Venture Capital Investment Firm

We are looking to overhaul our existing website (substantially), with only using the same logos (which we can provide).
We are an investment firm that focuses on making loans to late stage technology companies. Our site should ultimately look like other venture capital firms, and look modern and fresh. We have an existing website www.northvaleloan.com which this will be replacing, although we will be using a lot of the existing written content, and potentially the numbers of pages we will need, we are not wed to anything else. Please feel free to shoot any questions at any time and thank you in advance for your help!
Websites we like as examples:
https://www.tkbrandel.com/
https://www.emberwoodfunds.com/
Target Market(s)
Potential investors who will invest in our firm, as well as potentially companies that are looking to borrow money from us.

```html
<!DOCTYPE html>
<html lang="en">
<head>
<meta charset="utf-8">
<title>Northvale IP — Investment Partners</title>
<link href="https://fonts.googleapis.com/css2?family=Lora:wght@700&family=Roboto:wght@400;500&family=Open+Sans:wght@400;600;700&display=swap" rel="stylesheet">
<style>
:root{
  --navy:#1b2a36;
  --nav-grad:#2b4a5c;
  --blue:#2f9bd6;
  --ink:#1d1d1d;
  --muted:#5b5b5b;
  --orange:#d9662a;
  --ring:#b3dcec;
  --footer:#161a1d;
  --footer-band:#101315;
}
*{box-sizing:border-box;margin:0;padding:0}
html,body{width:1200px;height:3432px;overflow:hidden}
body{position:relative;background:#fff;font-family:"Roboto",sans-serif;color:var(--ink)}
.abs{position:absolute}

/* header */
.brand{left:112px;top:20px;display:flex;align-items:center;gap:14px}
.brand-dot{width:46px;height:46px;border-radius:50%;background:var(--navy)}
.brand-name{font-family:"Lora",serif;font-weight:700;font-size:34px;color:var(--navy);line-height:1}
.brand-sub{font-family:"Lora",serif;font-weight:700;font-size:10px;color:var(--navy);letter-spacing:.5px;margin-top:4px}
.phone{left:754px;top:8px;display:flex;align-items:center;gap:14px;font-size:22px;color:var(--navy)}
.phone-ring{width:46px;height:46px;border:2px solid var(--navy);border-radius:50%;display:flex;align-items:center;justify-content:center}
.signup{left:1012px;top:20px;font-size:14px;font-weight:500;color:var(--navy)}
.mainnav{left:386px;top:61px;width:814px;height:48px;background:linear-gradient(90deg,var(--nav-grad),var(--navy));clip-path:polygon(32px 0,100% 0,100% 100%,0 100%)}
.mainnav ul{list-style:none;display:flex;gap:38px;padding-left:60px;height:100%;align-items:center}
.mainnav li{color:#fff;font-size:14px;font-weight:500}
.mainnav li.active{color:var(--blue)}

/* hero */
.hero{left:0;top:109px;width:1200px;height:538px;
  background:
    linear-gradient(180deg,rgba(255,255,255,0) 70%,rgba(60,50,45,.55) 100%),
    linear-gradient(90deg,#5b4a3e 0%,#8d8a86 12%,#b9c3cb 22%,#3d3c40 33%,#9aa6b0 45%,#d6dade 58%,#eceeef 70%,#c9c9c9 82%,#5e5e5e 92%,#3f4a3a 100%)}
.hero-box{left:681px;top:221px;width:519px;height:282px;background:rgba(60,60,60,.72);padding:34px 0 0 30px;color:#fff}
.hero-box h1{font-family:"Lora",serif;font-weight:700;font-size:46px;line-height:1}
.hero-box p{font-family:"Lora",serif;font-weight:700;font-size:17px;line-height:28px;margin-top:22px;width:440px}
.btn-out{display:inline-block;border:2px solid currentColor;border-radius:28px;font-weight:500;font-size:15px}
.hero-box .btn-out{margin-top:18px;padding:14px 30px}
.dots{left:574px;top:583px;display:flex;gap:6px}
.dots span{width:13px;height:13px;border:1.5px solid #fff;border-radius:50%}
.dots span.on{background:#fff;width:16px;height:16px;margin-top:-1px}

/* about */
.about-art{left:196px;top:695px;width:318px;height:318px;border-radius:50%;
  background:conic-gradient(from 200deg,#d9b48a,#7c6a5a,#3d4d63,#9aa8b8,#e9e6e1,#c9a47c,#d9b48a);
  box-shadow:0 4px 14px rgba(0,0,0,.25)}
.about{left:599px;top:700px;width:500px}
.eyebrow{color:var(--blue);font-size:17px}
.about h2{font-family:"Lora",serif;font-weight:700;font-size:25px;margin-top:10px;white-space:nowrap}
.about h3{font-size:14px;font-weight:400;margin-top:12px}
.about p{width:452px;font-size:14px;line-height:25.8px;color:var(--muted);text-align:justify;margin-top:14px}
.about .btn-out{margin-top:20px;padding:14px 32px;color:var(--ink);font-size:15px}

/* services */
.services{left:0;top:1156px;width:1200px;height:617px;background:linear-gradient(160deg,#eef1f4,#dfe5ec 60%,#eef1f5)}
.sec-title{width:1200px;text-align:center;font-family:"Lora",serif;font-weight:700;font-size:38px;color:var(--ink)}
.sub{width:1200px;text-align:center;font-size:14px;line-height:34px}
.card{width:459px;height:277px;border-radius:6px;box-shadow:0 4px 12px rgba(0,0,0,.25)}
.card-label{width:459px;text-align:center;font-size:21px;font-weight:500}

/* team */
.member{width:300px;text-align:center}
.ring{margin:0 auto;width:260px;height:260px;border-radius:50%;background:var(--ring);padding:12px;position:relative}
.ring .photo{width:236px;height:236px;border-radius:50%;background:radial-gradient(circle at 50% 38%,#9a9a9a 0,#5a5a5a 22%,#1a1a1a 48%),linear-gradient(#111,#222)}
.stem{width:30px;height:24px;background:var(--ring);margin:-6px auto 0}
.overlay{position:absolute;left:12px;top:170px;width:236px;height:78px;border-radius:0 0 118px 118px;background:rgba(47,120,170,.7);display:flex;justify-content:center;gap:16px;padding-top:16px}
.overlay span{width:10px;height:10px;background:#fff;border-radius:2px}
.m-name{font-size:21px;font-weight:500;margin-top:26px}
.m-role{font-size:16px;font-weight:600;color:var(--orange);margin-top:12px;font-family:"Open Sans",sans-serif}
.m-spec{font-size:14px;font-weight:600;margin-top:10px;font-family:"Open Sans",sans-serif}

/* news */
.news{left:0;top:2420px;width:1200px;height:786px;background:linear-gradient(180deg,#f0f0f0,#e4e4e4)}
.news .sub,.news-sub{font-family:"Open Sans",sans-serif;font-size:14px;line-height:28px;color:#444}
.feature-img{left:123px;top:2651px;width:500px;height:369px;background:linear-gradient(100deg,#2e2e2e 0%,#6b6b6b 25%,#bdbdbd 45%,#e0e0e0 60%,#9a9a9a 80%,#3c3c3c 100%)}
.feature-card{left:181px;top:2844px;width:450px;height:186px;background:#fff;padding:16px;box-shadow:0 2px 8px rgba(0,0,0,.2);font-family:"Open Sans",sans-serif}
.tag{display:inline-block;background:var(--blue);color:#fff;font-size:13px;font-weight:700;padding:5px 11px}
.date{display:inline-block;font-size:14px;color:#555;margin-left:8px}
.date::before{content:"";display:inline-block;width:11px;height:11px;background:var(--blue);margin-right:6px;vertical-align:-1px}
.news-title{font-family:"Lora",serif;font-weight:700;font-size:17px;margin-top:14px;white-space:nowrap}
.news-text{font-size:13px;line-height:28px;color:#555;margin-top:2px}
.news-text span{display:block;white-space:nowrap}
.more{font-size:14px;font-weight:700;color:var(--blue)}
.arrows{left:600px;top:2951px}
.arrows span{display:block;width:26px;height:26px;background:#555;margin-bottom:8px;color:#fff;font-size:14px;text-align:center;line-height:26px}
.thumb{width:156px;height:176px}
.side{left:815px;width:300px;font-family:"Open Sans",sans-serif}
.view-more{left:518px;top:3081px;width:164px;height:52px;border:2px solid var(--navy);border-radius:28px;font-size:15px;font-weight:500;text-align:center;line-height:48px}

/* footer */
.footer{left:0;top:3206px;width:1200px;height:226px;background:var(--footer)}
.footer-band{left:0;top:3206px;width:1200px;height:50px;background:var(--footer-band)}
.footnav{top:3220px;color:#fff;font-size:15px;font-weight:500;display:flex;gap:40px}
.footer-dot{left:538px;top:3177px;width:120px;height:120px;border-radius:50%;background:#fff}
.f-label{top:3284px;color:#fff;font-size:15px;font-weight:500}
.socials{left:336px;top:3327px;display:flex;gap:7px}
.socials span{width:32px;height:32px;background:#1f4f8a}
.email{left:662px;top:3322px;width:217px;height:40px;background:#fff;font-family:"Open Sans",sans-serif;font-size:14px;color:#888;padding:11px 14px}
.submit{left:886px;top:3322px;width:113px;height:40px;background:var(--blue);color:#fff;font-weight:700;font-size:16px;text-align:center;line-height:40px}
.copy{left:0;top:3396px;width:1200px;text-align:center;color:#fff;font-size:14px;font-family:"Open Sans",sans-serif}
</style>
</head>
<body>

<div class="abs brand"><div class="brand-dot"></div><div><div class="brand-name">Northvale IP</div><div class="brand-sub">INVESTMENT PARTNERS, LLC</div></div></div>
<div class="abs phone"><div class="phone-ring"><svg width="22" height="22" viewBox="0 0 24 24"><path d="M6.6 10.8a15 15 0 0 0 6.6 6.6l2.2-2.2c.3-.3.7-.4 1-.2 1.1.4 2.3.6 3.6.6.6 0 1 .4 1 1V20c0 .6-.4 1-1 1A17 17 0 0 1 3 4c0-.6.4-1 1-1h3.5c.6 0 1 .4 1 1 0 1.3.2 2.5.6 3.6.1.3 0 .7-.2 1z" fill="#1b2a36"/></svg></div>+1 555 014 2290</div>
<div class="abs signup">&#9679; SIGN UP</div>
<nav class="abs mainnav"><ul><li class="active">HOME</li><li>STRATEGY</li><li>ABOUT US</li><li>TEAM</li><li>NEWS</li><li>CONTACT</li><li>INVESTORS</li></ul></nav>

<div class="abs hero" role="img" aria-label="Business partners shaking hands across a meeting table in a glass office"></div>
<div class="abs hero-box"><h1>NORTHVALE IP</h1><p>Lorem ipsum dolor sit amet, consectetur adipiscing elit, sed do eiusmod tempor incididunt</p><span class="btn-out">GET STARTED</span></div>
<div class="abs dots"><span></span><span class="on"></span><span></span></div>

<div class="abs about-art" role="img" aria-label="Round emblem filled with office and finance photography"></div>
<div class="abs about">
  <div class="eyebrow">About us</div>
  <h2>NORTHVALE IP STARTED WITH A BIG IDEA</h2>
  <h3>FINANCE PROVEN INNOVATION WITH A DIFFERENT APPROACH</h3>
  <p>Northvale IP is a private investment firm unique in its dual focus on life science and technology credit opportunities. Our ambidextrous approach to investing reflects a broad recognition and appreciation for the critical role intellectual property plays in the successful commercialization of products. We apply our extensive industry expertise to assess the revenue visibility created by these assets and offer a range of creative financing solutions.</p>
  <span class="btn-out">READ MORE &#10148;</span>
</div>

<div class="abs services"></div>
<div class="abs sec-title" style="left:0;top:1218px">OUR SERVICES</div>
<div class="abs sub" style="left:0;top:1272px">WE ARE A GLOBAL STRUCTURED CREDIT INVESTMENT FIRM FOCUSED<br>ON THEHEALTHCARE AND TECHNOLOGY INDUSTRIES</div>
<div class="abs card" style="left:112px;top:1377px;background:linear-gradient(180deg,rgba(255,255,255,0) 60%,#f3f1ee 80%),linear-gradient(90deg,#4a3b33 0%,#c9b8a8 14%,#2e3a52 32%,#f0eeec 50%,#5a7fa8 62%,#f5f4f2 72%,#3a3e48 88%,#e9e7e4 100%)" role="img" aria-label="Colleagues discussing documents at a healthcare meeting"></div>
<div class="abs card" style="left:627px;top:1377px;background:linear-gradient(100deg,#f4f5f7 0%,#1e2a44 22%,#2f62b8 40%,#d8914a 55%,#2e5fb4 70%,#0d2a63 100%)" role="img" aria-label="Handshake over a glowing technology chart"></div>
<div class="abs card-label" style="left:112px;top:1671px">HEALTHCARE</div>
<div class="abs card-label" style="left:627px;top:1671px">TECHNOLOGY INDUSTRIES</div>

<div class="abs sec-title" style="left:0;top:1866px">OUR SENIOR TEAM</div>
<div class="abs member" style="left:124px;top:1948px"><div class="ring"><div class="photo" role="img" aria-label="Portrait of Elias Marrow"></div></div><div class="stem"></div><div class="m-name">ELIAS MARROW</div><div class="m-role">MANAGING PARTNER</div><div class="m-spec">Life Sciences, Technology</div></div>
<div class="abs member" style="left:448px;top:1948px"><div class="ring"><div class="photo" role="img" aria-label="Portrait of Tarek Osmani"></div><div class="overlay"><span></span><span></span><span></span></div></div><div class="stem"></div><div class="m-name">TAREK OSMANI</div><div class="m-role">MANAGING PARTNER</div><div class="m-spec">Technology</div></div>
<div class="abs member" style="left:770px;top:1948px"><div class="ring"><div class="photo" role="img" aria-label="Portrait of Owen Hartley"></div></div><div class="stem"></div><div class="m-name">OWEN HARTLEY</div><div class="m-role">PARTNER</div><div class="m-spec">Chief Operating Officer</div></div>

<div class="abs news"></div>
<div class="abs sec-title" style="left:0;top:2492px">LATEST FROM NEWS</div>
<div class="abs sub news-sub" style="left:0;top:2563px">It's important to understanding your options since not every mortgage is built the same. We offer an array of loan options to<br>satisfy most borrower's needs, understanding that every homeowner is different.</div>
<div class="abs feature-img" role="img" aria-label="Two smiling colleagues in an office"></div>
<div class="abs feature-card">
  <span class="tag">CLARA WHITFIELD</span><span class="date">April 30, 2018</span>
  <div class="news-title">NORTHVALE IP COMPLETES STRUCTURED DEBT</div>
  <div class="news-text"><span>Northvale IP Investment Partners (“Northvale IP”) announced</span><span>today that it has completed a structured debt investment in</span></div>
  <div class="more">READ MORE &#187;</div>
</div>
<div class="abs arrows"><span>&#8250;</span><span style="background:#888">&#8249;</span></div>

<div class="abs thumb" style="left:649px;top:2651px;background:linear-gradient(150deg,#3a3a3a 0%,#8c8c8c 35%,#e8e8e8 60%,#cfd6dc 100%)" role="img" aria-label="Laptop, calculator and financial papers on a desk"></div>
<div class="abs side" style="top:2660px"><span class="tag">ADMIN</span><span class="date" style="margin-left:18px">OCT 19, 2016</span><div class="news-title">NORTHVALE IP COMPLETES</div><div class="news-text"><span>Northvale IP Investment Partners (“Northvale IP”)</span><span>announced today that it has</span></div><div class="more">READ MORE &#187;</div></div>
<div class="abs thumb" style="left:649px;top:2856px;background:linear-gradient(90deg,#2c3442 0%,#c8ccd0 30%,#3b4250 50%,#e2e4e6 70%,#2d3540 100%)" role="img" aria-label="Business team greeting with a handshake"></div>
<div class="abs side" style="top:2866px"><span class="tag">ADMIN</span><span class="date" style="margin-left:18px">April 4, 2018</span><div class="news-title">HALVERD SEMICONDUCTOR</div><div class="news-text"><span>Lumetra Optics, Inc., a leading supplier of</span><span>advanced semiconductor communications</span></div><div class="more">READ MORE &#187;</div></div>
<div class="abs view-more">VIEW MORE &#10148;</div>

<div class="abs footer"></div>
<div class="abs footer-band"></div>
<div class="abs footnav" style="left:235px"><span>HOME</span><span>STRATEGY</span><span>ABOUT US</span></div>
<div class="abs footnav" style="left:679px"><span>TEAM</span><span>NEWS</span><span>CONTACT</span><span>INVESTORS</span></div>
<div class="abs footer-dot"></div>
<div class="abs f-label" style="left:403px">FOLLOW US ON.</div>
<div class="abs f-label" style="left:660px">NEWSLETTER</div>
<div class="abs socials"><span></span><span></span><span></span><span></span><span></span></div>
<div class="abs email">Email Address</div>
<div class="abs submit">SUBMIT</div>
<div class="abs copy">© Copyrights Northvaleip. All Rights Reserved</div>

</body>
</html>
```